Brantwell Tax Advisers Business Card

We are seeking a clean, professional, and modern double sided business card design for Brantwell Tax Advisers, a tax, accounting, and advisory firm serving business owners, professionals, and investors.
The design should convey credibility, precision, trust, and sophistication appropriate for a CPA level tax advisory firm. Avoid playful, trendy, or overly decorative styles. The look should be sharp, balanced, and timeless.
Our official company logo has been uploaded, which must be incorporated appropriately and consistently with the brand. Designers should not modify, distort, or recreate the logo.
Card format
Standard US business card size (3.5 x 2 inches)
Double sided
Design direction
Professional and modern
Minimalist and uncluttered
Strong typography and clean spacing
Subtle visual interest is welcome, but simplicity is preferred
High contrast and readability are critical
Front side
Primary focus on the Brantwell Tax Advisers logo
The firm name should be clearly legible and visually prominent
Background may be white or dark, depending on what best complements the logo
Back side
Contact information layout, such as
Name: Martin G. Pellow, MSA, CFP®, AIF®, EA
Title: Managing Director, Tax
Email: mpellow@mybrantwell.net
Website: https://www.corvelfirm-example.tax/
Mobile: (480) 555-0132
Direct: (817) 555-0187
Main: (817) 555-0149
Address: 3807 Fenwick Rd., Suite 118, Grapevine, TX 76099
Icons may be used sparingly if they enhance clarity
The layout should feel organized and structured
Color and style
Use colors that complement the uploaded logo
Neutral, professional tones preferred
Avoid loud or saturated colors
The design should print well on standard cardstock
Print considerations
Design should be print‑ready
No edge to edge elements that risk being cut off
Proper margins and bleed awareness
Overall, the goal is a polished, high end business card that reflects trust, expertise, and professionalism consistent with a firm providing tax strategy, compliance, and advisory services.

```html
<!DOCTYPE html>
<html lang="en">
<head>
<meta charset="utf-8">
<title>Brantwell Tax Advisers Business Card</title>
<link href="https://fonts.googleapis.com/css2?family=Montserrat:wght@400;500;600;700&display=swap" rel="stylesheet">
<style>
  :root {
    --navy: #23265e;
    --orange: #f47a30;
    --ink: #2a2a2e;
    --paper: #ffffff;
    --backdrop: #1e1e1f;
  }
  * { margin: 0; padding: 0; box-sizing: border-box; }
  html, body {
    width: 1200px; height: 1200px; overflow: hidden;
    background: var(--backdrop);
    font-family: "Montserrat", sans-serif;
  }
  .card {
    position: absolute;
    left: 179px;
    width: 861px;
    height: 496px;
    background: var(--paper);
    box-shadow: 0 10px 30px rgba(0,0,0,.45);
  }
  .card--front { top: 84px; }
  .card--back { top: 621px; }

  .brand__mark {
    position: absolute;
    left: 196px; top: 212px;
    width: 30px; height: 30px;
    background: var(--orange);
  }
  .brand__name {
    position: absolute;
    left: 282px; top: 180px;
    color: var(--navy);
    font-weight: 600;
    line-height: 1;
  }
  .brand__firm {
    display: block;
    font-size: 50px;
    letter-spacing: 5px;
    text-transform: uppercase;
  }
  .brand__descriptor {
    display: block;
    font-size: 31px;
    letter-spacing: 7px;
    margin-top: 14px;
  }

  .person {
    position: absolute;
    left: 39px; top: 37px;
  }
  .person__name {
    color: var(--navy);
    font-weight: 700;
    font-size: 30px;
    letter-spacing: .2px;
  }
  .person__title {
    color: var(--ink);
    font-weight: 400;
    font-size: 25px;
    margin-top: 2px;
  }

  .contacts {
    position: absolute;
    left: 37px; top: 302px;
    list-style: none;
  }
  .contacts__item {
    display: flex; align-items: center;
    gap: 12px;
    color: var(--ink);
    font-size: 25px;
    line-height: 41px;
  }
  .contacts__icon { width: 26px; height: 22px; fill: var(--navy); flex: none; }

  .office {
    position: absolute;
    right: 42px; top: 350px;
    text-align: right;
    color: var(--ink);
    font-size: 25px;
    line-height: 35px;
    font-style: normal;
  }
  .office__web-domain { color: var(--orange); }
</style>
</head>
<body>

<section class="card card--front">
  <span class="brand__mark"></span>
  <div class="brand__name">
    <span class="brand__firm">Brantwell</span>
    <span class="brand__descriptor">Tax Advisers</span>
  </div>
</section>

<section class="card card--back">
  <div class="person">
    <div class="person__name">Martin G. Pellow, MSA, CFP®, AIF®, EA</div>
    <div class="person__title">Managing Director, Tax</div>
  </div>

  <ul class="contacts">
    <li class="contacts__item">
      <svg class="contacts__icon" viewBox="0 0 24 24" aria-hidden="true">
        <path d="M6.6 10.8c1.4 2.8 3.8 5.1 6.6 6.6l2.2-2.2c.3-.3.7-.4 1-.2 1.1.4 2.3.6 3.6.6.6 0 1 .4 1 1V20c0 .6-.4 1-1 1C10.6 21 3 13.4 3 4c0-.6.4-1 1-1h3.5c.6 0 1 .4 1 1 0 1.3.2 2.5.6 3.6.1.3 0 .7-.2 1z"/>
      </svg>
      <span>(480) 555-0132</span>
    </li>
    <li class="contacts__item">
      <svg class="contacts__icon" viewBox="0 0 26 22" aria-hidden="true">
        <path d="M1 7c0-3 5-5 12-5s12 2 12 5v2h-6V6.5c-2-.7-4-1-6-1s-4 .3-6 1V9H1z"/>
        <path d="M7 10h12l4 6v5H3v-5z"/>
      </svg>
      <span>(817) 555-0187</span>
    </li>
    <li class="contacts__item">
      <svg class="contacts__icon" viewBox="0 0 26 22" aria-hidden="true">
        <path d="M1 7c0-3 5-5 12-5s12 2 12 5v2h-6V6.5c-2-.7-4-1-6-1s-4 .3-6 1V9H1z"/>
        <path d="M7 10h12l4 6v5H3v-5z"/>
      </svg>
      <span>(817) 555-0149</span>
    </li>
    <li class="contacts__item">
      <svg class="contacts__icon" viewBox="0 0 26 20" aria-hidden="true">
        <path d="M2 3h22v14H2z M3.5 4.5l9.5 7 9.5-7v1.6l-9.5 7-9.5-7z" fill-rule="evenodd"/>
      </svg>
      <span>mpellow@mybrantwell.net</span>
    </li>
  </ul>

  <address class="office">
    3807 Fenwick Rd., Suite 118,<br>
    Grapevine, TX 76099<br>
    www.<span class="office__web-domain">brantwell-example</span>.tax
  </address>
</section>

</body>
</html>
```